Flyer-Design für Immobilienmakler
Zielgruppe
Wir sind seit 1992 Immobilienmakler und möchten einen Flyer zur Präsentation unserer Firma und Objektakquise gestalten lassen.
Dieser soll einen Gutschein für eine kostenlose Immobilienbewertung enthalten.
Aufgabenstellung
Wir lassen uns dann überraschen

```html
<!DOCTYPE html>
<html lang="de">
<head>
<meta charset="utf-8">
<title>Gutschein Immobilienbewertung – Postkarte</title>
<link rel="stylesheet" href="https://fonts.googleapis.com/css2?family=Montserrat:wght@700&family=Poppins:ital,wght@0,300;0,400;1,300&display=swap">
<style>
  :root {
    --blue: #2472c4;
    --blue-light: #2a9be0;
    --grey-dark: #5f5f5f;
    --grey-mid: #c6c6c6;
    --grey-stamp: #6c6c6c;
    --ink: #1d1d1d;
    --photo-top: #4d8fd6;
    --photo-bottom: #a7c3de;
    --stage: #e9ebef;
  }
  * { margin: 0; padding: 0; box-sizing: border-box; }
  html, body { width: 1199px; height: 1200px; overflow: hidden; }
  body { background: var(--stage); position: relative; font-family: "Poppins", sans-serif; }

  .card {
    position: absolute; left: 219px;
    width: 810px; height: 575px;
    transform: scale(0.938); transform-origin: top left;
    overflow: hidden;
    box-shadow: 0 8px 22px rgba(0,0,0,.18);
  }
  .card--front { top: 36px; }
  .card--back { top: 624px; background: linear-gradient(135deg, #e6e6e6 0%, #ffffff 45%, #f7f7f7 75%, #e4e4e4 100%); }

  /* Front */
  .front__photo {
    position: absolute; left: 0; top: 0; width: 810px; height: 452px;
    background: linear-gradient(180deg, var(--photo-top) 0%, var(--photo-bottom) 100%);
  }
  .front__title {
    position: absolute; left: 0; top: 82px; width: 348px; height: 95px;
    background: var(--blue);
    color: #fff; font-family: "Montserrat", sans-serif; font-weight: 700;
    font-size: 50px; line-height: 95px; letter-spacing: 0;
    white-space: nowrap; padding-left: 4px;
  }
  .offer {
    position: absolute; left: 428px; top: 300px; width: 360px; height: 150px;
    background: rgba(255,255,255,.78);
    transform: rotate(-5deg);
    padding: 14px 0 0 30px;
    color: var(--ink); font-weight: 300;
  }
  .offer__lead { font-size: 25px; line-height: 26px; padding-left: 80px; }
  .offer__line { font-size: 38px; line-height: 34px; letter-spacing: -0.5px; white-space: nowrap; }
  .offer__line em { font-style: normal; color: var(--blue-light); }
  .offer__note { font-size: 17px; font-style: italic; padding-left: 68px; line-height: 22px; }

  .front__band { position: absolute; left: 0; top: 452px; width: 810px; height: 26px; background: var(--blue); }
  .front__footer { position: absolute; left: 0; top: 478px; width: 810px; height: 97px; background: var(--grey-dark); }
  .front__logo {
    position: absolute; left: 422px; top: 8px; width: 46px; height: 46px; border-radius: 50%;
    background: #fff; color: var(--ink); font-size: 10px; font-style: italic; font-weight: 300;
    display: flex; align-items: center; justify-content: center;
  }
  .front__claim {
    position: absolute; right: 16px; top: 45px;
    color: #fff; font-weight: 300; font-size: 21px; white-space: nowrap;
  }

  /* Back */
  .back__divider { position: absolute; left: 405px; top: 0; width: 1px; height: 545px; background: #d2d2d2; }
  .back__intro {
    position: absolute; left: 70px; top: 32px;
    font-size: 12.5px; line-height: 15px; text-transform: uppercase; color: var(--ink); font-weight: 400;
  }
  .back__ribbon {
    position: absolute; left: 0; top: 90px; width: 405px; height: 25px; background: var(--blue);
    color: #fff; font-size: 12px; font-weight: 300; line-height: 25px; padding-left: 70px;
  }
  .options { position: absolute; left: 47px; top: 153px; list-style: none; }
  .options li { height: 58px; display: flex; align-items: flex-start; font-size: 17.5px; color: var(--ink); white-space: nowrap; }
  .options li::before {
    content: ""; width: 26px; height: 26px; border: 3px solid var(--blue); margin-right: 15px; flex: none;
  }
  .field { position: absolute; left: 48px; width: 335px; }
  .field__line { height: 22px; background: var(--grey-mid); }
  .field__label { font-size: 10px; line-height: 14px; color: var(--ink); }
  .field--name { top: 404px; } .field--address { top: 452px; } .field--phone { top: 501px; }
  .back__band { position: absolute; left: 0; top: 545px; width: 810px; height: 30px; background: var(--blue); }
  .back__band::after { content: ""; position: absolute; left: 405px; top: 0; width: 1px; height: 30px; background: rgba(255,255,255,.35); }

  .stamp {
    position: absolute; left: 680px; top: 35px; width: 93px; height: 121px; background: var(--grey-stamp);
    color: #fff; font-size: 9px; font-weight: 400; display: flex; align-items: center; justify-content: center;
  }
  .carrier { position: absolute; left: 427px; top: 153px; color: var(--ink); font-size: 16px; line-height: 17px; }
  .carrier i { display: block; font-weight: 300; }
  .sender-logo {
    position: absolute; left: 435px; top: 232px; width: 111px; height: 111px; border-radius: 50%;
    background: var(--grey-stamp); color: #fff; font-size: 9px;
    display: flex; align-items: center; justify-content: center;
  }
  .sender-address { position: absolute; left: 427px; top: 398px; font-size: 30px; line-height: 32px; color: var(--ink); white-space: nowrap; }
</style>
</head>
<body>

<section class="card card--front" aria-label="Vorderseite Gutschein">
  <div class="front__photo" role="img" aria-label="Foto eines Einfamilienhauses mit Garten unter blauem Himmel"></div>
  <div class="front__title">GUTSCHEIN</div>
  <div class="offer">
    <p class="offer__lead">Konstenlose</p>
    <p class="offer__line">BEWERTUNG</p>
    <p class="offer__line">IHRER <em>IMMOBILIE</em></p>
    <p class="offer__note">*Im Wert von 800€</p>
  </div>
  <div class="front__band"></div>
  <div class="front__footer">
    <div class="front__logo">Ihr Logo</div>
    <p class="front__claim">Ihr Immobilienmakler seit 1992</p>
  </div>
</section>

<section class="card card--back" aria-label="Rückseite Antwortkarte">
  <div class="back__divider"></div>
  <p class="back__intro">Gerne stellen wir Ihnen aktuelle<br>Informationen zum Immobilienmarkt<br>in Ihrer Region zur Verfügung.</p>
  <p class="back__ribbon">Ja, bitte senden Sie mir Informationen zu!</p>
  <ul class="options">
    <li>Immobilien verkaufen/vermieten</li>
    <li>Immobilien kaufen/mieten</li>
    <li>Immobilienbewertung</li>
    <li>Verwaltung von Immobilien</li>
  </ul>
  <div class="field field--name"><div class="field__line"></div><p class="field__label">Name</p></div>
  <div class="field field--address"><div class="field__line"></div><p class="field__label">Adresse</p></div>
  <div class="field field--phone"><div class="field__line"></div><p class="field__label">Telefonnummer</p></div>

  <div class="stamp">Briefmarke</div>
  <p class="carrier">Briefwerk Nord<i>Antwort</i></p>
  <div class="sender-logo">Logo von Ihnen</div>
  <p class="sender-address">Ihre Daten wie<br>Name des Unternehmen<br>Straße<br>Postleitzahl &amp; Ort</p>
  <div class="back__band"></div>
</section>

</body>
</html>
```